Riverstone & Pine Construction and Developments business cards

A business card with watermark background (construction work)

Company logo attached

Home improvement projects
House renovations
Bathroom and kitchen renovations
House extensions
New builds and granny flats

Director Omar Haddine
(Phone number)
omar@rpcbuildgroup.com.au
(Instagram logo) rpc_buildgroup

```html
<!DOCTYPE html>
<html lang="en">
<head>
<meta charset="utf-8">
<title>Riverstone &amp; Pine Construction – Business Cards</title>
<link rel="stylesheet" href="https://fonts.googleapis.com/css2?family=Open+Sans:wght@700&family=Poppins:wght@400;500&display=swap">
<style>
  :root {
    --stage: #e9e9e7;
    --card: #ffffff;
    --brand-blue: #3a7bbf;
    --brand-blue-light: #4f8cca;
    --ink: #3c3c3c;
    --ink-soft: #555555;
    --band-grey: #4a4a4a;
  }
  * { margin: 0; padding: 0; box-sizing: border-box; }
  html, body { width: 1200px; height: 960px; overflow: hidden; }
  body { background: var(--stage); position: relative; font-family: "Poppins", sans-serif; }

  .card {
    position: absolute;
    left: 275px;
    width: 650px;
    background: var(--card);
    box-shadow: 0 4px 14px rgba(0,0,0,0.18);
    overflow: hidden;
  }
  .card--front { top: 87px; height: 372px; }
  .card--back { top: 500px; height: 371px; }

  .front-panel { position: absolute; inset: 0; }

  .wordmark {
    position: absolute;
    color: var(--brand-blue);
    font-family: "Poppins", sans-serif;
    font-weight: 500;
    text-align: center;
    line-height: 1.25;
  }
  .wordmark__mark {
    display: block;
    width: 16px; height: 16px;
    margin: 0 auto 8px;
    background: var(--brand-blue);
  }
  .card--front .wordmark { left: 22px; width: 190px; top: 140px; font-size: 16px; }
  .card--back .wordmark { left: 225px; width: 200px; top: 52px; font-size: 17px; }
  .wordmark__sub { display: block; font-size: 0.72em; letter-spacing: 0.5px; }

  .services {
    position: absolute;
    right: 0;
    top: 182px;
    list-style: none;
    font-family: "Open Sans", sans-serif;
    font-weight: 700;
    font-size: 14.5px;
    color: #ffffff;
    text-align: right;
  }
  .services li {
    display: flex;
    align-items: center;
    justify-content: flex-end;
    height: 27.4px;
    letter-spacing: 0.2px;
  }
  .services li::after {
    content: "";
    display: block;
    width: 28px; height: 5px;
    margin-left: 13px;
    background: #ffffff;
    border-radius: 3px 0 0 3px;
  }

  .person { position: absolute; left: 165px; top: 252px; }
  .person__name { color: var(--brand-blue); font-size: 16.5px; font-weight: 500; letter-spacing: 0.2px; line-height: 1.2; }
  .person__role { color: var(--ink-soft); font-size: 14.5px; line-height: 1.2; }

  .divider { position: absolute; left: 325px; top: 235px; width: 1px; height: 73px; background: var(--brand-blue); }

  .contacts { position: absolute; left: 346px; top: 238px; list-style: none; color: var(--ink); font-size: 13px; }
  .contacts li { display: flex; align-items: center; height: 22px; }
  .contacts svg, .contacts .icon-square { width: 12px; height: 12px; margin-right: 8px; flex: none; }
  .icon-square { display: inline-block; background: var(--brand-blue); border-radius: 2px; width: 10px !important; height: 10px !important; margin-left: 1px; }

  .footer-band { position: absolute; left: 0; bottom: 0; width: 650px; height: 18px; }
</style>
</head>
<body>

<section class="card card--front" aria-label="Business card front">
  <svg class="front-panel" width="650" height="372" viewBox="0 0 650 372">
    <defs>
      <linearGradient id="worksite-tone" x1="0" y1="0" x2="1" y2="1">
        <stop offset="0" stop-color="#4a88c7" stop-opacity="0.55"/>
        <stop offset="1" stop-color="#3a7bbf" stop-opacity="0"/>
      </linearGradient>
    </defs>
    <polygon points="328,0 650,0 650,372 242,372" fill="var(--brand-blue)"/>
    <polygon points="328,0 650,0 650,372 242,372" fill="url(#worksite-tone)" role="img" aria-label="Faint watermark photo of a builder working at a brick wall"/>
  </svg>

  <div class="wordmark">
    <span class="wordmark__mark"></span>
    Riverstone &amp; Pine
    <span class="wordmark__sub">Construction and Developments</span>
  </div>

  <ul class="services">
    <li>HOME IMPROVEMENT</li>
    <li>HOUSE RENOVATIONS</li>
    <li>KITCHEN RENOVATIONS</li>
    <li>BATHROOM RENOVATIONS</li>
    <li>HOUSE EXTENSIONS</li>
    <li>NEW BUILDS AND GRANNY FLATS</li>
  </ul>
</section>

<section class="card card--back" aria-label="Business card back">
  <div class="wordmark">
    <span class="wordmark__mark"></span>
    Riverstone &amp; Pine
    <span class="wordmark__sub">Construction and Developments</span>
  </div>

  <div class="person">
    <p class="person__name">OMAR HADDINE</p>
    <p class="person__role">Director</p>
  </div>

  <div class="divider"></div>

  <ul class="contacts">
    <li>
      <svg viewBox="0 0 24 24" aria-hidden="true"><path fill="var(--brand-blue)" d="M6.6 10.8a15.1 15.1 0 0 0 6.6 6.6l2.2-2.2a1 1 0 0 1 1-.25 11.4 11.4 0 0 0 3.6.57 1 1 0 0 1 1 1V20a1 1 0 0 1-1 1A17 17 0 0 1 3 4a1 1 0 0 1 1-1h3.5a1 1 0 0 1 1 1c0 1.25.2 2.45.57 3.57a1 1 0 0 1-.25 1z"/></svg>
      +00 11 444 5555
    </li>
    <li>
      <svg viewBox="0 0 24 24" aria-hidden="true"><path fill="var(--brand-blue)" d="M2 5h20v14H2z"/><path fill="none" stroke="#fff" stroke-width="1.8" d="M2.5 6l9.5 7 9.5-7"/></svg>
      omar@rpcbuildgroup.com.au
    </li>
    <li>
      <span class="icon-square" aria-hidden="true"></span>
      rpc_buildgroup
    </li>
  </ul>

  <svg class="footer-band" width="650" height="18" viewBox="0 0 650 18" aria-hidden="true">
    <polygon points="0,0 330,0 325,18 0,18" fill="var(--brand-blue)"/>
    <polygon points="333,0 650,0 650,18 328,18" fill="var(--band-grey)"/>
  </svg>
</section>

</body>
</html>
```